Brenton High 20 year Reunion Memorial

I need a tasteful memorial poster with the names of those alumni that have deceased. The school colors are black, orange, silver and white. I would definately like the background to be black. At the top of the poster I would like it to read:
Brenton Hight School Class of 1993.
This evening is dedicated in memory of
(followed by the names on the attached file

Industry/Entity Type

School

Requirements
Must have
• Black background

```html
<!DOCTYPE html>
<html lang="en">
<head>
<meta charset="utf-8">
<title>Brenton High School Class of 1993 – Memorial</title>
<link rel="stylesheet" href="https://fonts.googleapis.com/css2?family=Playfair+Display:ital,wght@1,400&display=swap">
<style>
  :root {
    --stage: #e4e4e4;
    --poster-black: #231f20;
    --school-orange: #f7941d;
    --text-white: #ffffff;
    --serif: "Playfair Display", Georgia, serif;
  }
  * { margin: 0; padding: 0; box-sizing: border-box; }
  html, body {
    width: 1200px;
    height: 1200px;
    overflow: hidden;
    background: var(--stage);
  }
  .poster {
    position: absolute;
    left: 180px;
    top: 41px;
    width: 840px;
    height: 1118px;
    background: var(--poster-black);
    color: var(--text-white);
    font-family: var(--serif);
    font-style: italic;
    font-weight: 400;
  }
  .poster-frame {
    position: absolute;
    inset: 0;
    width: 840px;
    height: 1118px;
  }
  .poster-frame path {
    fill: none;
    stroke: var(--school-orange);
    stroke-width: 4;
  }
  .line {
    position: absolute;
    left: 0;
    width: 100%;
    text-align: center;
    line-height: 1;
    white-space: nowrap;
    font-weight: 400;
    font-style: italic;
  }
  .school-name { top: 138px; font-size: 68px; }
  .class-year { top: 244px; font-size: 40px; }
  .dedication { top: 386px; font-size: 58px; }
  .dedication-sub { top: 477px; font-size: 58px; }

  .memorial {
    position: absolute;
    width: 360px;
    transform: translateX(-50%);
    text-align: center;
    line-height: 1;
    white-space: nowrap;
  }
  .memorial-name { display: block; font-size: 38px; }
  .memorial-dates { display: block; font-size: 17px; margin-top: 8px; }
  .col-left { left: 222px; }
  .col-right { left: 594px; }
  .col-center { left: 420px; }
  .row-1 { top: 599px; }
  .row-2 { top: 712px; }
  .row-3 { top: 826px; }
  .row-4 { top: 949px; }
</style>
</head>
<body>
  <main class="poster">
    <svg class="poster-frame" viewBox="0 0 840 1118" aria-hidden="true">
      <path d="M86 44 H754 A42 42 0 0 0 796 86 V1032 A42 42 0 0 0 754 1074 H86 A42 42 0 0 0 44 1032 V86 A42 42 0 0 0 86 44 Z"/>
    </svg>

    <h1 class="line school-name">Brenton High School</h1>
    <p class="line class-year">Class of 1993</p>
    <p class="line dedication">This evening is dedicated</p>
    <p class="line dedication-sub">In Memory Of</p>

    <div class="memorial col-left row-1">
      <span class="memorial-name">Anna Whitcombe</span>
      <span class="memorial-dates">March 3, 1975 - October 14, 1994</span>
    </div>
    <div class="memorial col-right row-1">
      <span class="memorial-name">Grant Ellery</span>
      <span class="memorial-dates">June 18, 1975 - May 9, 1998</span>
    </div>
    <div class="memorial col-left row-2">
      <span class="memorial-name">Paul Dennison</span>
      <span class="memorial-dates">March 11, 1975 - July 8, 2003</span>
    </div>
    <div class="memorial col-right row-2">
      <span class="memorial-name">Victor Halloway</span>
      <span class="memorial-dates">October 2, 1974 - March 19, 2009</span>
    </div>
    <div class="memorial col-left row-3">
      <span class="memorial-name">Rachel Ambrose</span>
      <span class="memorial-dates">June 5, 1975 - April 24, 2011</span>
    </div>
    <div class="memorial col-right row-3">
      <span class="memorial-name">Lydia Carmody</span>
      <span class="memorial-dates">February 9, 1975 - November 3, 2012</span>
    </div>
    <div class="memorial col-center row-4">
      <span class="memorial-name">Evan Whitlock</span>
      <span class="memorial-dates">May 16, 1975 - March 12, 2013</span>
    </div>
  </main>
</body>
</html>
```